Marvel Brookworks highend custom homes

We build high end custom homes and timber frames we specialize in rustic hand made designs along with iron and concrete accents to add a modern touch 90% of my homes are buit on lake front properries attached is my logo and slogan as of now and my previous one

Target Market(s)

High end custom homes

Industry/Entity Type

Custom residential construction

Contact Information for Business Card

Been in buissness 8+ years inssured and reliable

Colors
A7469A
B969AE
D3A5CF
EDDBEB
F8F0F9

Requirements
Must have
• Must have slogan and phone number
Should not have
• A combination of rustic yet modern accents

```html
<!DOCTYPE html>
<html lang="en">
<head>
<meta charset="utf-8">
<title>Marvel Brookworks – Business Card</title>
<link rel="stylesheet" href="https://fonts.googleapis.com/css2?family=Jost:wght@600;700&family=Lato:wght@300;400&display=swap">
<style>
  :root {
    --backdrop: #e4e4e4;
    --card: #ffffff;
    --forest: #4e5b4a;
    --forest-light: #5f6d5a;
    --forest-dark: #434f40;
    --ink: #1f1f1f;
    --band-text: #dfe4dc;
  }
  * { box-sizing: border-box; margin: 0; padding: 0; }
  html, body {
    width: 1200px; height: 1200px; overflow: hidden;
    background: var(--backdrop);
  }
  .card {
    position: absolute; left: 185px;
    width: 830px; height: 488px;
    background: var(--card);
    overflow: hidden;
  }
  .card--front { top: 81px; }
  .card--back { top: 631px; }

  .brand { display: flex; flex-direction: column; }
  .brand__row { display: flex; align-items: center; gap: 16px; }
  .brand__square { width: 40px; height: 40px; background: var(--forest); flex: none; }
  .brand__name {
    font-family: "Jost", sans-serif; font-weight: 700;
    color: var(--forest); font-size: 50px; letter-spacing: 0.5px;
    text-transform: uppercase; line-height: 1.02;
  }
  .slogan {
    display: flex; align-items: center; gap: 9px;
    font-family: "Lato", sans-serif; font-weight: 400;
    font-size: 17px; letter-spacing: 0.6px; color: var(--ink);
    text-transform: uppercase; margin-top: 16px; white-space: nowrap;
  }
  .slogan__dot {
    width: 7px; height: 7px; border-radius: 50%;
    background: var(--ink); border: 1.5px solid #8a8a8a; flex: none;
  }

  .card--front .brand {
    position: absolute; left: 0; right: 0; top: 130px;
    align-items: center;
  }

  .card--back .brand {
    position: absolute; left: 65px; top: 92px;
    align-items: flex-start;
  }
  .card--back .brand__square { width: 34px; height: 34px; }
  .card--back .brand__name { font-size: 40px; }
  .card--back .slogan { font-size: 15px; margin-top: 14px; }

  .contact-list {
    position: absolute; right: 45px; top: 136px;
    list-style: none;
    font-family: "Lato", sans-serif; font-weight: 400;
    font-size: 22px; color: var(--ink);
  }
  .contact-list li {
    display: flex; align-items: center; justify-content: flex-end;
    gap: 14px; height: 31px;
  }
  .icon { width: 20px; height: 20px; flex: none; }

  .band { position: absolute; left: 0; top: 300px; width: 830px; height: 130px; }
  .address {
    position: absolute; right: 45px; top: 349px;
    list-style: none;
    font-family: "Lato", sans-serif; font-weight: 300;
    font-size: 22px; color: var(--band-text);
  }
  .address li { display: flex; align-items: center; justify-content: flex-end; gap: 14px; height: 32px; }
  .address__spacer { width: 20px; flex: none; }
</style>
</head>
<body>

<section class="card card--front">
  <div class="brand">
    <div class="brand__row">
      <span class="brand__square"></span>
      <span class="brand__name">Marvel<br>Brookworks</span>
    </div>
    <p class="slogan"><span class="slogan__dot"></span>Crafted by the Lakeshore<span class="slogan__dot"></span></p>
  </div>
</section>

<section class="card card--back">
  <div class="brand">
    <div class="brand__row">
      <span class="brand__square"></span>
      <span class="brand__name">Marvel<br>Brookworks</span>
    </div>
    <p class="slogan"><span class="slogan__dot"></span>Crafted by the Lakeshore<span class="slogan__dot"></span></p>
  </div>

  <ul class="contact-list">
    <li>+61 408 555 219
      <svg class="icon" viewBox="0 0 20 20" aria-hidden="true">
        <rect width="20" height="20" rx="4" fill="#4e5b4a"/>
        <path d="M6.5 4.5l2 2.2-1.2 1.4c.7 1.6 1.9 2.8 3.5 3.6l1.4-1.2 2.2 2-1.3 2c-4.2-.5-7.5-3.8-8-8z" fill="#fff"/>
      </svg>
    </li>
    <li>info@marvelbrookworks.com
      <svg class="icon" viewBox="0 0 20 20" aria-hidden="true">
        <rect width="20" height="20" rx="4" fill="#4e5b4a"/>
        <rect x="4" y="6" width="12" height="8.5" fill="none" stroke="#fff" stroke-width="1.4"/>
        <path d="M4 6l6 5 6-5" fill="none" stroke="#fff" stroke-width="1.4"/>
      </svg>
    </li>
    <li>www.marvelbrookworks.com
      <svg class="icon" viewBox="0 0 20 20" aria-hidden="true">
        <rect width="20" height="20" rx="4" fill="#4e5b4a"/>
        <circle cx="10" cy="10" r="5.5" fill="none" stroke="#fff" stroke-width="1.4"/>
        <path d="M4.5 10h11M10 4.5c-2.4 3-2.4 8 0 11M10 4.5c2.4 3 2.4 8 0 11" fill="none" stroke="#fff" stroke-width="1.1"/>
      </svg>
    </li>
  </ul>

  <svg class="band" viewBox="0 0 830 130" aria-hidden="true">
    <rect x="0" y="37" width="830" height="82" fill="#4e5b4a"/>
    <polygon points="196,37 255,12 255,119 196,119" fill="#5f6d5a"/>
    <polygon points="255,12 315,37 315,119 255,119" fill="#434f40"/>
  </svg>

  <ul class="address">
    <li>PO Box 240
      <svg class="icon" viewBox="0 0 20 20" aria-hidden="true">
        <path d="M10 3.5a4 4 0 0 1 4 4c0 3-4 7-4 7s-4-4-4-7a4 4 0 0 1 4-4z" fill="#dfe4dc"/>
        <circle cx="10" cy="7.5" r="1.5" fill="#4e5b4a"/>
        <path d="M5 16h10" stroke="#dfe4dc" stroke-width="1.4"/>
      </svg>
    </li>
    <li>Harlow Bay SA 0000<span class="address__spacer"></span></li>
  </ul>
</section>

</body>
</html>
```